HARLOWE CONSERVATORY SAXOPHONE SENIOR RECITAL

I need a poster design for my senior saxophone recital. The title of it is "Quill: a Voyage beneath the Edge of Tone". My concept is completely contrasting to the idea of a typical university recital. I'm so put off by the idea of "clap..clap..{play some music}..clap..clap..repeat". My recital is all based off of sound. The music I selected is all very modern (i.e Brem Ostrakel 'Warm from the First Pour' for Saxophone and Coffee Machine). I've included the Chatterbox link so you can see the picture I have in the background. I like the idea of minimal black and white photography. Also, I would like the time / date / location / etc. all included on it. Let your imaginations run wild! It's art for an artist!
https://www.chatterbox-example.net/events/412093857716230/
Target Market(s)
University Students around the Harlowe Conservatory and locals around the art district of South Beach, FL.
Industry/Entity Type
University
Look and feel

```html
<!DOCTYPE html>
<html lang="en">
<head>
<meta charset="utf-8">
<title>Quill — A Voyage Beneath the Edge of Tone</title>
<link rel="stylesheet" href="https://fonts.googleapis.com/css2?family=Roboto+Condensed:wght@700&family=Questrial&display=swap">
<style>
  :root {
    --stage: #e4e4e4;
    --poster-black: #050505;
    --photo-mid: #2a2a2a;
    --photo-light: #8c8c8c;
    --title-panel: rgba(140, 140, 140, 0.78);
    --title-ink: #111111;
    --info-ink: #d2d2d2;
    --divider: #9a9a9a;
  }
  * { box-sizing: border-box; margin: 0; padding: 0; }
  html, body {
    width: 1200px;
    height: 786px;
    overflow: hidden;
    background: var(--stage);
  }
  .poster {
    position: absolute;
    left: 326px;
    top: 0;
    width: 548px;
    height: 786px;
    background: var(--poster-black);
    overflow: hidden;
  }
  .poster__photo {
    position: absolute;
    inset: 0;
    background:
      radial-gradient(ellipse 45% 28% at 62% 18%, var(--photo-light) 0%, rgba(140,140,140,0) 70%),
      radial-gradient(ellipse 22% 30% at 22% 40%, #6a6a6a 0%, rgba(106,106,106,0) 70%),
      radial-gradient(ellipse 30% 35% at 55% 45%, var(--photo-mid) 0%, rgba(42,42,42,0) 80%),
      var(--poster-black);
  }
  .title-panel {
    position: absolute;
    left: 86px;
    top: 493px;
    width: 377px;
    height: 239px;
    background: var(--title-panel);
    color: var(--title-ink);
    font-family: "Roboto Condensed", "Arial Narrow", sans-serif;
    font-weight: 700;
    text-align: center;
    text-transform: uppercase;
  }
  .title-panel__name {
    display: block;
    font-size: 112px;
    line-height: 1;
    letter-spacing: 6px;
    margin-top: 2px;
  }
  .title-panel__line {
    display: block;
    font-size: 30px;
    line-height: 32px;
    letter-spacing: 1.5px;
  }
  .title-panel__line--small { font-size: 24px; line-height: 30px; }
  .title-panel__line--large {
    font-size: 44px;
    line-height: 46px;
    letter-spacing: 1.5px;
    margin-top: 4px;
  }
  .event-info {
    position: absolute;
    left: 86px;
    top: 733px;
    width: 377px;
    height: 49px;
    display: flex;
    justify-content: space-between;
    align-items: center;
    font-family: "Questrial", "Century Gothic", sans-serif;
    font-size: 25px;
    letter-spacing: 1.5px;
    color: var(--info-ink);
    text-transform: uppercase;
  }
  .event-info__divider {
    width: 1px;
    height: 49px;
    background: var(--divider);
  }
</style>
</head>
<body>
  <main class="poster">
    <div class="poster__photo" role="img" aria-label="Minimal black and white photograph of a woman lying on dark fabric, arms folded over her head, face hidden"></div>

    <h1 class="title-panel">
      <span class="title-panel__name">Quill</span>
      <span class="title-panel__line">A Voyage Beneath</span>
      <span class="title-panel__line title-panel__line--small">The</span>
      <span class="title-panel__line title-panel__line--large">Edge of Tone</span>
    </h1>

    <p class="event-info">
      <span class="event-info__item">Location</span>
      <span class="event-info__divider"></span>
      <span class="event-info__item">Date</span>
      <span class="event-info__divider"></span>
      <span class="event-info__item">Time</span>
    </p>
  </main>
</body>
</html>
```